Wheels Open Doors - Two sided invitation to encourage bike friendly businesses

Pedal Haven is a charitable trust who want to grow everyday bike use. One way to do that is help businesses understand that 'Wheels Open Doors'. We want a postcard sized 'invitation' that bike users can give to their favourite businesses, inviting them to find out more about all the benefits of attracting bike users to their business and becoming a 'Pedal Haven Business'. We are currently finalising copy, so the attached is indicative but not final copy. The docx file is the words, the png is indicative of the type of infographic we might want to feature.
I'm also attaching a mock up of our window sticker for businesses, and some social shares featuring photographic images which we have available to use. This will give you an idea of our branding to date. Our extended branding concept (which we will use when we re-do our website) is based on icons, so I'm open to seeing icon focused designs also.
The feel needs to be inviting, credible, enticing, business like, noticeable, with a strong call to action.

Target Market(s)

Small business operators: retail, cafes, etc; also managers of larger chains such as supermarkets, gyms, etc.

Industry/Entity Type

Non Profit

Font styles to use
Serif
Other font styles liked:
• Logo is done in Raleway, so need compatible font.

Colors
9ccb3b

Requirements
Must have
• Two Sides
• Use the copy provided
• Strong call to action - visiting website
• Use our colours
• A6 sized cards
Nice to have
• Compelling images and/or infographic
• Consistency with circles / curves used in other branding.
Should not have
• Not bland, not something that will get lost on the recipients desk or counter.

```html
<!DOCTYPE html>
<html lang="en">
<head>
<meta charset="utf-8">
<title>Wheels Open Doors – Pedal Haven invitation card</title>
<link rel="stylesheet" href="https://fonts.googleapis.com/css2?family=Oswald:wght@400;500;600&family=Barlow+Semi+Condensed:wght@400;500;600&display=swap">
<style>
  :root {
    --green: #1f8a3c;
    --green-deep: #16702f;
    --green-dark: #0f5a25;
    --green-light: #9ccb3b;
    --orange: #f5a623;
    --pale: #eef4ec;
    --white: #ffffff;
    --ink: #2b2b2b;
    --page: #eceeea;
  }
  * { box-sizing: border-box; margin: 0; padding: 0; }
  html, body { width: 1200px; height: 1000px; overflow: hidden; }
  body { background: var(--page); position: relative; font-family: "Barlow Semi Condensed", sans-serif; }

  .card { position: absolute; overflow: hidden; box-shadow: 0 6px 18px rgba(0,0,0,.18); }

  /* Front */
  .card-front { left: 60px; top: 80px; width: 640px; height: 460px; z-index: 2; }
  .front-backdrop { position: absolute; inset: 0; background: radial-gradient(circle at 70% 40%, #2a9a47, var(--green) 55%, var(--green-deep)); }
  .brand { position: absolute; display: flex; align-items: center; gap: 10px; }
  .brand-front { left: 40px; top: 42px; }
  .brand-dot { width: 48px; height: 48px; border-radius: 50%; background: var(--white); }
  .brand-name { font-family: "Oswald", sans-serif; font-weight: 500; font-size: 24px; color: var(--white); }
  .front-url { position: absolute; left: 40px; top: 118px; font-family: "Oswald", sans-serif; font-weight: 500; font-size: 15px; letter-spacing: .5px; color: var(--orange); }
  .headline { position: absolute; left: 42px; top: 200px; font-family: "Oswald", sans-serif; font-weight: 500; color: var(--white); line-height: 1.12; font-size: 24px; text-transform: uppercase; }
  .headline .accent { display: block; color: var(--orange); font-size: 54px; line-height: 1; margin-top: 4px; }
  .headline .tail { display: block; color: var(--orange); font-size: 26px; }

  .infographic { position: absolute; left: 282px; top: 40px; width: 350px; height: 390px; }

  /* Back */
  .card-back { left: 520px; top: 470px; width: 630px; height: 480px; background: var(--white); z-index: 1; }
  .back-circle { position: absolute; left: 300px; top: -10px; width: 330px; height: 330px; border-radius: 50%; background: var(--pale); }
  .back-circle-inner { position: absolute; left: 345px; top: 35px; width: 240px; height: 240px; border-radius: 50%; background: radial-gradient(circle at 40% 40%, #2a9a47, var(--green-deep)); display: flex; align-items: center; justify-content: center; }
  .back-title { font-family: "Oswald", sans-serif; font-weight: 500; font-size: 28px; color: var(--orange); text-align: center; line-height: 1.1; }
  .back-title .word { font-weight: 600; }

  .back-copy { position: absolute; left: 40px; top: 90px; width: 570px; color: var(--ink); }
  .reasons { width: 295px; list-style: none; font-size: 16px; line-height: 1.22; }
  .reasons li { margin-bottom: 2px; }
  .reasons .num { color: var(--green); font-weight: 600; }
  .heart { display: inline-block; width: 14px; height: 13px; vertical-align: -1px; }
  .study { margin-top: 14px; font-size: 15.5px; line-height: 1.25; }
  .cta { margin-top: 10px; font-family: "Oswald", sans-serif; font-weight: 500; font-size: 14.5px; line-height: 1.25; color: var(--green); text-transform: uppercase; }
  .visit { margin-top: 10px; width: 360px; font-size: 15.5px; line-height: 1.25; }
  .visit strong { color: var(--green); font-weight: 600; }
  .brand-back { right: 36px; bottom: 28px; }
  .brand-back .brand-dot { width: 38px; height: 38px; background: var(--green); }
  .brand-back .brand-name { color: var(--green); font-size: 19px; }
</style>
</head>
<body>

<section class="card card-front" aria-label="Invitation card front">
  <div class="front-backdrop" role="img" aria-label="Soft green photographic background of parked bicycles"></div>

  <div class="brand brand-front">
    <span class="brand-dot"></span>
    <span class="brand-name">Pedal Haven</span>
  </div>
  <p class="front-url">WWW.PEDALHAVEN.ORG.NZ</p>

  <h1 class="headline">
    Why make<br>biking customers<br>— and their $$$ —
    <span class="accent">Welcome</span>
    <span class="tail">at your business?</span>
  </h1>

  <svg class="infographic" viewBox="0 0 350 390" aria-label="Infographic: one car park versus six bike parks in 13 square metres">
    <circle cx="170" cy="195" r="175" fill="#ffffff" fill-opacity=".18"/>
    <circle cx="170" cy="195" r="150" fill="#eef4ec"/>
    <rect x="62" y="95" width="200" height="80" rx="30" fill="#f5a623" role="img" aria-label="Car icon with a $27.00 per hour tag"/>
    <text x="162" y="142" text-anchor="middle" font-family="Barlow Semi Condensed, sans-serif" font-size="11" fill="#1f8a3c">$27.00 per hour</text>
    <line x1="40" y1="205" x2="292" y2="205" stroke="#555" stroke-width="1.5"/>
    <line x1="40" y1="198" x2="40" y2="212" stroke="#555" stroke-width="1.5"/>
    <line x1="292" y1="198" x2="292" y2="212" stroke="#555" stroke-width="1.5"/>
    <rect x="142" y="192" width="50" height="24" fill="#eef4ec"/>
    <text x="166" y="210" text-anchor="middle" font-family="Oswald, sans-serif" font-size="15" fill="#333">13m²</text>
    <rect x="50" y="228" width="172" height="84" rx="14" fill="#1f8a3c" fill-opacity=".85" role="img" aria-label="Six bicycle icons, each tagged $16.20 per hour"/>
    <g font-family="Barlow Semi Condensed, sans-serif" font-size="11" fill="#ffffff" text-anchor="middle">
      <text x="84" y="262">$16.20</text><text x="136" y="262">$16.20</text><text x="188" y="262">$16.20</text>
      <text x="84" y="294">$16.20</text><text x="136" y="294">$16.20</text><text x="188" y="294">$16.20</text>
    </g>
    <circle cx="280" cy="60" r="56" fill="#ffffff" fill-opacity=".4"/>
    <circle cx="280" cy="60" r="48" fill="#f5a623" stroke="#ffffff" stroke-width="4"/>
    <text x="280" y="72" text-anchor="middle" font-family="Oswald, sans-serif" font-weight="500" font-size="26" fill="#ffffff">$27.00</text>
    <circle cx="283" cy="318" r="62" fill="#ffffff" fill-opacity=".35"/>
    <circle cx="283" cy="318" r="54" fill="#0f5a25" stroke="#ffffff" stroke-width="4"/>
    <text x="283" y="332" text-anchor="middle" font-family="Oswald, sans-serif" font-weight="500" font-size="28" fill="#ffffff">$97.20</text>
  </svg>
</section>

<section class="card card-back" aria-label="Invitation card back">
  <div class="back-circle"></div>
  <div class="back-circle-inner">
    <h2 class="back-title">WHY <span class="word">WELCOME</span><br>BIKES?</h2>
  </div>

  <div class="back-copy">
    <ol class="reasons">
      <li><span class="num">1.</span> Biking customers spend $$$ where parking’s easy.</li>
      <li><span class="num">2.</span> They spend $$$ locally as they must carry what they buy.</li>
      <li><span class="num">3.</span> Biking customers move slower, so see what your business offers.</li>
      <li><span class="num">4.</span> They tell friends where’s good to park and shop, where they feel welcome.</li>
      <li><span class="num">5.</span> You’re helping people be environmentally, budget and heart friendly – and they’ll
        <svg class="heart" viewBox="0 0 14 13" aria-label="love"><path d="M7 12.5 1.2 6.8A3.4 3.4 0 0 1 7 2.2a3.4 3.4 0 0 1 5.8 4.6Z" fill="#e0343a"/></svg> you for it.</li>
    </ol>

    <p class="study">A Melbourne study showed swapping a car park for six bike parks could increase the space’s retail spend from $27 to $97.20 an hour.</p>
    <p class="cta">Just think – every bike parked by someone else’s business could have been your customer.</p>
    <p class="visit">See <strong>pedalhaven.org.nz</strong> to see how you can become a Pedal Haven Business.</p>
  </div>

  <div class="brand brand-back">
    <span class="brand-dot"></span>
    <span class="brand-name">Pedal Haven</span>
  </div>
</section>

</body>
</html>
```